need this made into a high quality editable copy...

mock this exact image and file, i created it in AI...but now i need the same thing created to where i can edit the text, add my own stuff, etc...mimic the colors, backgrounds, water, lighting, everything!

```html
<!DOCTYPE html>
<html lang="en">
<head>
<meta charset="utf-8">
<title>The Ocean Healed My Eczema – Label</title>
<link href="https://fonts.googleapis.com/css2?family=Montserrat:wght@300;400;500;700;800&display=swap" rel="stylesheet">
<style>
  :root {
    --deep-navy: #113f54;
    --sky-light: #9fd0da;
    --sky-pale: #b9dde3;
    --water-dark: #16506c;
    --water-mid: #3f86a3;
    --band-teal: #3a98ab;
    --panel-white: #e9ebf0;
    --foam-white: #eef0f3;
    --ink: #0c0c0c;
    --paper: #ffffff;
  }
  * { margin: 0; padding: 0; box-sizing: border-box; }
  html, body { width: 1200px; height: 849px; overflow: hidden; background: var(--paper); }
  body { position: relative; font-family: "Montserrat", Arial, sans-serif; }

  .label { position: absolute; top: 26px; width: 341px; overflow: hidden; }
  .label--front { left: 203px; height: 731px; }
  .label--back  { left: 664px; height: 740px; }

  .sky {
    position: absolute; left: 0; top: 0; width: 100%; height: 416px;
    background: linear-gradient(180deg, var(--deep-navy) 0%, var(--deep-navy) 30%, #2f7288 50%, #6eb2c2 75%, var(--sky-light) 100%);
  }
  .ocean {
    position: absolute; left: 0; top: 416px; width: 100%; bottom: 0;
    background: linear-gradient(180deg, #cfe9ee 0%, var(--water-dark) 2%, var(--water-mid) 10%, #5d9fb8 30%, #3c7f9f 70%, #4a8aa6 100%);
  }
  .label--back .sky { background: linear-gradient(180deg, var(--deep-navy) 0%, var(--deep-navy) 28%, #3e8296 48%, #76b9c8 75%, var(--sky-pale) 100%); }
  .label--back .ocean { height: 26px; bottom: auto;
    background: linear-gradient(180deg, #d5ecf0 0%, var(--water-dark) 15%, #2f7398 55%, #17496a 100%); }

  .line { position: absolute; display: block; line-height: 1; white-space: nowrap; text-transform: uppercase; }

  /* front headline */
  .headline { position: absolute; left: 32px; top: 0; width: 290px; height: 220px; color: var(--paper); font-weight: 700; }
  .headline .line { left: 0; }
  .headline__l1 { top: 54px; font-size: 44px; }
  .headline__l2 { top: 100px; font-size: 44px; }
  .headline__l3 { top: 141px; font-size: 62px; }

  /* front feature card */
  .feature-card {
    position: absolute; left: 22px; top: 478px; width: 296px; height: 131px;
    background: var(--panel-white); border-radius: 20px;
    color: var(--ink); font-weight: 800;
  }
  .feature-card .line { left: 0; right: 0; text-align: center; }
  .feature-card__l1 { top: 7px; font-size: 25.5px; }
  .feature-card__l2 { top: 47px; font-size: 24.5px; }
  .feature-card__l3 { top: 78px; font-size: 41px; }

  .intro-card {
    position: absolute; left: 22px; top: 616px; width: 296px; height: 59px;
    background: var(--panel-white); border-radius: 20px;
    color: var(--ink); font-weight: 500; font-size: 14.8px; line-height: 19px;
    padding: 10px 11px 0; white-space: nowrap;
    text-align: justify; text-align-last: justify;
  }

  .net-band { position: absolute; left: 0; bottom: 0; width: 100%; height: 43px; }
  .net-band__text {
    position: absolute; left: 0; right: 0; bottom: 10px; text-align: center;
    color: var(--paper); font-size: 19px; font-weight: 400; line-height: 1;
  }

  /* back */
  .back-heading { position: absolute; left: 30px; top: 0; width: 281px; height: 180px; color: var(--paper); font-weight: 800; }
  .back-heading .line { left: 0; right: 0; text-align: center; }
  .back-heading__l1 { top: 56px; font-size: 25.5px; }
  .back-heading__l2 { top: 95px; font-size: 24.5px; }
  .back-heading__l3 { top: 126px; font-size: 41px; }
  .back-intro {
    position: absolute; left: 29px; top: 186px; width: 282px;
    color: var(--paper); font-size: 15px; font-weight: 500; line-height: 19px;
    white-space: nowrap; text-align: justify; text-align-last: justify;
  }
  .body-panel {
    position: absolute; left: 0; top: 442px; width: 100%; height: 239px;
    background: linear-gradient(180deg, #dfe6ec 0%, var(--foam-white) 30%, #e6e9ee 100%);
  }
  .body-copy {
    position: absolute; left: 23px; top: 8px; width: 295px;
    color: var(--ink); font-weight: 300; font-size: 16px; line-height: 31.6px;
    white-space: nowrap; text-align: justify; text-align-last: justify;
  }
  .back-band { position: absolute; left: 0; bottom: 0; width: 100%; height: 59px; background: var(--band-teal); }
</style>
</head>
<body>
  <section class="label label--front">
    <div class="sky" role="img" aria-label="Stormy teal sky with soft clouds and a white lightning bolt"></div>
    <div class="ocean" role="img" aria-label="Rippling ocean water below the horizon"></div>

    <h1 class="headline">
      <span class="line headline__l1">The Ocean</span>
      <span class="line headline__l2">Healed My</span>
      <span class="line headline__l3">Eczema</span>
    </h1>

    <div class="feature-card">
      <span class="line feature-card__l1">Product Feature</span>
      <span class="line feature-card__l2">The Ocean Healed</span>
      <span class="line feature-card__l3">My Eczema</span>
    </div>

    <p class="intro-card">Lorem ipsum dolor sit amet, con-<br>sectetuer adipiscing elit, sed dia</p>

    <div class="net-band">
      <svg width="341" height="43" viewBox="0 0 341 43" aria-hidden="true">
        <path d="M3 43 L20 6 Q23 0 30 0 L311 0 Q318 0 321 6 L338 43 Z" fill="var(--band-teal)"/>
      </svg>
      <span class="net-band__text">Net. 4 OZ (118 ml)</span>
    </div>
  </section>

  <section class="label label--back">
    <div class="sky" role="img" aria-label="Teal gradient sky fading to a pale horizon"></div>
    <div class="ocean" role="img" aria-label="Thin band of dark ocean water at the horizon"></div>

    <div class="back-heading">
      <span class="line back-heading__l1">Product Feature</span>
      <span class="line back-heading__l2">The Ocean Healed</span>
      <span class="line back-heading__l3">My Eczema</span>
    </div>
    <p class="back-intro">Lorem ipsum dolor sit amet, con-<br>sectetuer adipiscing elit, sed dia</p>

    <div class="body-panel" role="img" aria-label="Pale foamy water surface behind the body copy">
      <p class="body-copy">Lorem ipsum dolor sit amet, consec-<br>tetuer adipiscing elit, sed diam<br>nonummy nibh euismod tincidunt<br>ut laoreet dolore magna aliquam<br>erat volutpat. Ut wisi enim ad minim<br>veniam, quis nostrud exerci tation<br>ullamcorper suscipit lobortis nisl ut</p>
    </div>
    <div class="back-band"></div>
  </section>
</body>
</html>
```